Business Consultants - Require an A4 size presentation folder with inserts for a new exciting Standa

We have developed a service/product where we help small and medium businesses to draft up their policies & procedures manual for their business. This manual has everything in it on how to run their business. From how to answer the phone, to how to process invoices, through to HR information, and marketing plans.

We need a professional but modern looking presentation folder to house all this information. The size will be A4. Inside we will have up to 12 inserts to seperate the different chapters/topic. For example. Sales, Marketing, Administration, Operations, Finance.

Each folder will be branded with the client logo and name on the front, hence it does need to be relativity simple and neutral as to not clash with their colours etc.

We will have our Logo and contact details on the back of the folder.

The design aspect may well come for the chapter inserts. Again the actual tabs will need to be neutral so that we can write on them so that when you open the front cover you can quickly go the chapter you need.

Be warned I do not want any generic design gallery type designs. They stand out as cheap and nasty. I need you actually put some thought into these !!!

Attached is our Logo, and a two photos of the sort of shape and size of the anticipated folders.

Target Market(s)

Small & Medium Brick & Mortar Business Owners

Industry/Entity Type

Business Consultant

Colors

Designer to choose colors to be used in the design.

Requirements
Must have
• Must be clean, crisp, but with some cool simple design elements
Should not have
• Too many bold colours as it will clash with our client logos, which we have no control over what colour they are

```html
<!DOCTYPE html>
<html lang="en">
<head>
<meta charset="utf-8">
<title>The Plan Crew – Manual Folder Set</title>
<link href="https://fonts.googleapis.com/css2?family=Open+Sans:wght@700&family=Questrial&display=swap" rel="stylesheet">
<style>
  :root{
    --paper:#ffffff;
    --frame:#9a9a9a;
    --ink:#333333;
    --label:#595959;
    --accent:#f26522;
    --footer:#3c3c3e;
    --strip:#d9d9da;
    --brand-blue:#29abe2;
    --brand-grey:#4d4d4f;
  }
  *{box-sizing:border-box;margin:0;padding:0}
  html,body{width:1200px;height:1000px;overflow:hidden;background:var(--paper)}
  body{position:relative;font-family:"Questrial",Arial,sans-serif;color:var(--ink)}
  .sheet{position:absolute;background:var(--paper);border:1px solid var(--frame);overflow:hidden}
  .sheet svg{position:absolute;inset:0;width:100%;height:100%}
  .caption{position:absolute;font-family:"Open Sans",Arial,sans-serif;font-weight:700;font-size:24px;color:var(--label);text-align:center;width:323px}

  .cover{left:37px;top:24px;width:323px;height:456px}
  .cover-logo{position:absolute;left:16px;top:53px;width:104px;height:104px;border-radius:50%;background:var(--paper);display:flex;align-items:center;justify-content:center;font-size:26px;color:#111}
  .cover-title{position:absolute;left:36px;top:334px;color:var(--accent);font-size:19px}
  .cover-list{position:absolute;left:36px;top:356px;list-style:none;color:var(--accent);font-size:11.5px;line-height:14px}
  .cover-band{position:absolute;left:0;right:0;bottom:0;height:16px;background:var(--footer)}

  .back{left:377px;top:24px;width:322px;height:456px}
  .brand-art{position:absolute;left:103px;top:204px;width:116px;height:74px;background:linear-gradient(180deg,#bdbdbf 0%,#6b6b6d 60%,#ffffff 100%);border-radius:3px}
  .brand-name{position:absolute;left:0;width:100%;top:286px;text-align:center;font-size:12px;letter-spacing:.3px;color:var(--brand-grey)}
  .back-footer{position:absolute;left:0;right:0;bottom:0;height:47px;background:var(--footer);border-top:2px solid #8c8c8e}
  .contact{position:absolute;display:flex;align-items:flex-start;gap:6px;color:#fff;font-size:8.5px;line-height:9px}
  .contact .dot{flex:0 0 12px;height:12px;border-radius:50%;background:var(--accent);display:flex;align-items:center;justify-content:center}
  .contact .dot svg{position:static;width:8px;height:8px}

  .index{left:725px;top:24px;width:323px;height:456px}
  .inside{left:37px;top:520px;width:323px;height:457px}
  .tab-title{font-family:"Questrial",Arial,sans-serif;font-size:8px;fill:#fff}
  .tab-note{font-family:"Questrial",Arial,sans-serif;font-size:4.4px;fill:#fff}

  .brand-lockup{position:absolute;left:850px;top:740px;width:270px;height:200px}
  .brand-lockup .brand-art{left:30px;top:0;width:240px;height:150px}
  .brand-lockup .brand-name{top:168px;font-size:25px;text-align:left;left:10px;letter-spacing:.5px}
</style>
</head>
<body>

<!-- Cover -->
<div class="sheet cover">
  <svg viewBox="0 0 323 456" preserveAspectRatio="none" aria-hidden="true">
    <polygon points="120,0 323,0 323,22 70,140" fill="#cfd0d2"/>
    <polygon points="0,165 260,225 323,205 323,275 0,298" fill="#d3d4d6"/>
    <polygon points="100,118 323,20 323,280" fill="#8c8d90"/>
    <polygon points="0,160 110,110 250,225 0,298" fill="#d6d7d9" opacity=".9"/>
    <polygon points="250,225 323,205 323,275" fill="#b4b5b7"/>
  </svg>
  <div class="cover-logo">Logo</div>
  <div class="cover-title">Manual 2017</div>
  <ul class="cover-list"><li>. text text text</li><li>. text text text</li><li>. text text text</li></ul>
  <div class="cover-band"></div>
</div>
<div class="caption" style="left:22px;top:482px">Cover</div>

<!-- Back -->
<div class="sheet back">
  <svg viewBox="0 0 322 456" preserveAspectRatio="none" aria-hidden="true">
    <polygon points="0,0 322,0 322,236 133,98 0,222" fill="#8b8c8e"/>
    <polygon points="0,0 100,0 133,98 0,222" fill="#a6a7a9"/>
    <polygon points="0,0 60,0 322,150 322,185 133,98" fill="#5f6062" opacity=".55"/>
    <polygon points="322,0 260,0 0,150 0,185 133,98" fill="#5f6062" opacity=".45"/>
    <polygon points="290,208 322,200 322,236" fill="#cfd0d2"/>
  </svg>
  <div class="brand-art" role="img" aria-label="Brand illustration: grey city skyline with a team of people"></div>
  <div class="brand-name">THE PLAN CREW</div>
  <div class="back-footer">
    <div class="contact" style="left:9px;top:6px"><span class="dot"><svg viewBox="0 0 10 10"><path d="M2 1l2 2-1 1.2q1 1.8 2.8 2.8L7 6l2 2-1.2 1.2Q3.5 8.5.8 2.2z" fill="#fff"/></svg></span>06 555 0142 - 021 55 01 873</div>
    <div class="contact" style="left:172px;top:6px"><span class="dot"><svg viewBox="0 0 10 10"><path d="M5 1a3 3 0 0 1 3 3c0 2-3 5-3 5S2 6 2 4a3 3 0 0 1 3-3z" fill="#fff"/><circle cx="5" cy="4" r="1" fill="#f26522"/></svg></span>14 Harbour Lane,<br>Westfield 4020</div>
    <div class="contact" style="left:9px;top:27px"><span class="dot"><svg viewBox="0 0 10 10"><rect x="1.5" y="2.5" width="7" height="5" fill="none" stroke="#fff"/><path d="M1.5 2.5l3.5 3 3.5-3" fill="none" stroke="#fff"/></svg></span>hello@theplancrew.co.nz</div>
    <div class="contact" style="left:172px;top:27px"><span class="dot"><svg viewBox="0 0 10 10"><circle cx="5" cy="5" r="3.5" fill="none" stroke="#fff"/><path d="M1.5 5h7M5 1.5v7" stroke="#fff" stroke-width=".8"/></svg></span>www.theplancrew.co.nz</div>
  </div>
</div>
<div class="caption" style="left:370px;top:482px">Back</div>

<!-- Shared tab parts -->
<svg width="0" height="0" style="position:absolute">
  <defs>
    <linearGradient id="g1"><stop offset="0" stop-color="#3aaa35"/><stop offset="1" stop-color="#1e9e45"/></linearGradient>
    <linearGradient id="g2"><stop offset="0" stop-color="#29abe2"/><stop offset="1" stop-color="#0a7bc4"/></linearGradient>
    <linearGradient id="g3"><stop offset="0" stop-color="#f7941d"/><stop offset="1" stop-color="#f15a24"/></linearGradient>
    <linearGradient id="g4"><stop offset="0" stop-color="#ec008c"/><stop offset="1" stop-color="#e3357b"/></linearGradient>
    <linearGradient id="g5"><stop offset="0" stop-color="#ffde17"/><stop offset="1" stop-color="#fbb03b"/></linearGradient>
    <linearGradient id="g6"><stop offset="0" stop-color="#0072bc"/><stop offset="1" stop-color="#1c75bc"/></linearGradient>
    <linearGradient id="g7"><stop offset="0" stop-color="#92278f"/><stop offset="1" stop-color="#5b2c8f"/></linearGradient>
    <linearGradient id="g8"><stop offset="0" stop-color="#39b54a"/><stop offset="1" stop-color="#00803e"/></linearGradient>
  </defs>
</svg>

<!-- Index page -->
<div class="sheet index">
  <svg viewBox="0 0 323 456" aria-hidden="false">
    <rect x="10" y="0" width="32" height="456" fill="var(--strip)"/>
    <g fill="none" stroke="#fff" stroke-width="3" stroke-opacity=".35"></g>

    <g transform="translate(0,12)">
      <polygon points="0,16 136,16 148,29 136,42 0,42" fill="url(#g1)"/>
      <g fill="none" stroke="#fff" stroke-width="2.5" stroke-opacity=".35"><polyline points="106,20 113,29 106,38"/><polyline points="114,20 121,29 114,38"/><polyline points="122,20 129,29 122,38"/></g>
      <rect x="8" y="0" width="38" height="40" fill="#8dc63f"/>
      <text x="27" y="28" text-anchor="middle" font-family="Open Sans,Arial,sans-serif" font-weight="700" font-size="22" fill="#fff">$</text>
      <text class="tab-title" x="50" y="24">Sales</text>
      <text class="tab-note" x="50" y="31">Text Text Text Text Text Text</text><text class="tab-note" x="50" y="36">Text Text</text>
    </g>

    <g transform="translate(0,69)">
      <polygon points="0,16 148,16 160,29 148,42 0,42" fill="url(#g2)"/>
      <g fill="none" stroke="#fff" stroke-width="2.5" stroke-opacity=".35"><polyline points="118,20 125,29 118,38"/><polyline points="126,20 133,29 126,38"/><polyline points="134,20 141,29 134,38"/></g>
      <rect x="8" y="0" width="38" height="40" fill="#5bc8f0"/>
      <rect x="17" y="13" width="20" height="14" rx="2" fill="#fff"/><rect x="23" y="9" width="8" height="5" rx="1" fill="none" stroke="#fff" stroke-width="1.5"/>
      <text class="tab-title" x="50" y="24">Marketing</text>
      <text class="tab-note" x="50" y="31">Text Text Text Text Text Text</text><text class="tab-note" x="50" y="36">Text Text</text>
    </g>

    <g transform="translate(0,126)">
      <polygon points="0,16 163,16 175,29 163,42 0,42" fill="url(#g3)"/>
      <g fill="none" stroke="#fff" stroke-width="2.5" stroke-opacity=".35"><polyline points="133,20 140,29 133,38"/><polyline points="141,20 148,29 141,38"/><polyline points="149,20 156,29 149,38"/></g>
      <rect x="8" y="0" width="38" height="40" fill="#faa634"/>
      <circle cx="27" cy="15" r="5.5" fill="#fff"/><path d="M17 31a10 9 0 0 1 20 0z" fill="#fff"/>
      <text class="tab-title" x="50" y="24">Administration</text>
      <text class="tab-note" x="50" y="31">Text Text Text Text Text Text</text><text class="tab-note" x="50" y="36">Text Text</text>
    </g>

    <g transform="translate(0,183)">
      <polygon points="0,16 190,16 202,29 190,42 0,42" fill="url(#g4)"/>
      <g fill="none" stroke="#fff" stroke-width="2.5" stroke-opacity=".35"><polyline points="160,20 167,29 160,38"/><polyline points="168,20 175,29 168,38"/><polyline points="176,20 183,29 176,38"/></g>
      <rect x="8" y="0" width="38" height="40" fill="#f06eaa"/>
      <g fill="#fff"><rect x="18" y="20" width="4" height="11"/><rect x="24" y="15" width="4" height="16"/><rect x="30" y="10" width="4" height="21"/></g>
      <text class="tab-title" x="50" y="24">Operations</text>
      <text class="tab-note" x="50" y="31">Text Text Text Text Text Text</text><text class="tab-note" x="50" y="36">Text Text</text>
    </g>

    <g transform="translate(0,240)">
      <polygon points="0,16 215,16 227,29 215,42 0,42" fill="url(#g5)"/>
      <g fill="none" stroke="#fff" stroke-width="2.5" stroke-opacity=".35"><polyline points="185,20 192,29 185,38"/><polyline points="193,20 200,29 193,38"/><polyline points="201,20 208,29 201,38"/></g>
      <rect x="8" y="0" width="38" height="40" fill="#fff200"/>
      <path d="M23 9h8l-2 4a9 9 0 1 1-4 0z" fill="#fff"/>
      <text x="27" y="27" text-anchor="middle" font-family="Open Sans,Arial,sans-serif" font-weight="700" font-size="10" fill="#f7b500">$</text>
      <text class="tab-title" x="50" y="24">Finance</text>
      <text class="tab-note" x="50" y="31">Text Text Text Text Text Text</text><text class="tab-note" x="50" y="36">Text Text</text>
    </g>

    <g transform="translate(0,297)">
      <polygon points="0,16 248,16 260,29 248,42 0,42" fill="url(#g6)"/>
      <g fill="none" stroke="#fff" stroke-width="2.5" stroke-opacity=".35"><polyline points="218,20 225,29 218,38"/><polyline points="226,20 233,29 226,38"/><polyline points="234,20 241,29 234,38"/></g>
      <rect x="8" y="0" width="38" height="40" fill="#2b8fd6"/>
      <circle cx="20" cy="16" r="4" fill="none" stroke="#fff" stroke-width="2.5" stroke-dasharray="2 1.2"/>
      <circle cx="30" cy="14" r="5" fill="#fff"/><path d="M21 31a9 8 0 0 1 18 0z" fill="#fff"/>
      <text class="tab-title" x="50" y="24">Human Resources</text>
      <text class="tab-note" x="50" y="31">Text Text Text Text Text Text</text><text class="tab-note" x="50" y="36">Text Text</text>
    </g>

    <g transform="translate(0,354)">
      <polygon points="0,16 276,16 288,29 276,42 0,42" fill="url(#g7)"/>
      <g fill="none" stroke="#fff" stroke-width="2.5" stroke-opacity=".35"><polyline points="246,20 253,29 246,38"/><polyline points="254,20 261,29 254,38"/><polyline points="262,20 269,29 262,38"/></g>
      <rect x="8" y="0" width="38" height="40" fill="#b0549d"/>
      <rect x="15" y="8" width="24" height="17" fill="none" stroke="#fff" stroke-width="2"/><rect x="25" y="25" width="4" height="5" fill="#fff"/><rect x="20" y="30" width="14" height="2" fill="#fff"/>
      <text class="tab-title" x="50" y="24">IT</text>
      <text class="tab-note" x="50" y="31">Text Text Text Text Text Text</text><text class="tab-note" x="50" y="36">Text Text</text>
    </g>

    <g transform="translate(0,411)">
      <polygon points="0,16 308,16 320,29 308,42 0,42" fill="url(#g8)"/>
      <g fill="none" stroke="#fff" stroke-width="2.5" stroke-opacity=".35"><polyline points="278,20 285,29 278,38"/><polyline points="286,20 293,29 286,38"/><polyline points="294,20 301,29 294,38"/></g>
      <rect x="8" y="0" width="38" height="40" fill="#1fa64a"/>
      <path d="M22 18v-4a5 5 0 0 1 10 0" fill="none" stroke="#fff" stroke-width="2"/><rect x="19" y="18" width="16" height="13" fill="#fff"/><rect x="26" y="22" width="2" height="5" fill="#1fa64a"/>
      <text class="tab-title" x="50" y="24">Policies</text>
      <text class="tab-note" x="50" y="31">Text Text Text Text Text Text</text><text class="tab-note" x="50" y="36">Text Text</text>
    </g>
  </svg>
</div>
<div class="caption" style="left:725px;top:482px">Index page</div>

<!-- Page inside -->
<div class="sheet inside">
  <svg viewBox="0 0 323 457">
    <rect x="11" y="0" width="33" height="457" fill="var(--strip)"/>
    <g fill="#fff">
      <circle cx="28" cy="72" r="3"/><circle cx="28" cy="124" r="3"/><circle cx="28" cy="176" r="3"/><circle cx="28" cy="228" r="3"/>
      <circle cx="28" cy="280" r="3"/><circle cx="28" cy="332" r="3"/><circle cx="28" cy="384" r="3"/><circle cx="28" cy="436" r="3"/>
    </g>
    <g transform="translate(1,11)">
      <polygon points="0,16 137,16 149,29 137,42 0,42" fill="url(#g1)"/>
      <g fill="none" stroke="#fff" stroke-width="2.5" stroke-opacity=".35"><polyline points="107,20 114,29 107,38"/><polyline points="115,20 122,29 115,38"/><polyline points="123,20 130,29 123,38"/></g>
      <rect x="8" y="0" width="38" height="40" fill="#8dc63f"/>
      <text x="27" y="28" text-anchor="middle" font-family="Open Sans,Arial,sans-serif" font-weight="700" font-size="22" fill="#fff">$</text>
      <text class="tab-title" x="50" y="24">Sales</text>
      <text class="tab-note" x="50" y="31">Text Text Text Text Text Text</text><text class="tab-note" x="50" y="36">Text Text</text>
    </g>
  </svg>
  <div class="caption" style="left:-12px;top:406px">Page inside</div>
</div>

<!-- Brand lockup -->
<div class="brand-lockup">
  <div class="brand-art" role="img" aria-label="Brand illustration: grey city skyline with a team of people and their reflection"></div>
  <div class="brand-name">THE PLAN CREW</div>
</div>

</body>
</html>
```